Premium men's gut health supplement needs a bottle label designed

We’re velnora - a premium men’s wellness brand focused on gut health. Our first product is a high-quality daily supplement designed to support digestion, regularity, and internal cleanliness. Backed by science and tailored for modern lifestyles, velnora is crafted in the UK and proudly LGBT-owned. It aims to resolve intimacy problems that gay men may experience due to poor digestion but also does not exclude any other orientation - other men may use it simply to improve their digestion.

velnora is for health-conscious men who value science-backed supplements and want to feel confident from the inside out. Many of our early adopters will be gay and bisexual men who prioritise gut health as part of their self-care, sexual, and hygiene routine, though the product is equally effective and appealing to anyone seeking premium digestive support.

The product is premium the target customer is male, not specific to one location but primary markets will be US, UK and EU.

I’d like a supplement bottle designed for velnora, our premium men’s gut health brand. The focus should be clean, slightly clinical, and minimal - inspired by brands like Quelrin and Darvo. The key element is the wordmark (velnora) on the front, with no additional logo or icon. Lowercase text and a strong, contemporary font are preferred.

The bottle should be aesthetically pleasing so that people are proud to display it on their shelf, instead of hiding it in a cupboard (like Quelrin, darvo, Pia Venturek, Morvanel etc)

Avoid anything that shows the product as being for LGBT, e.g., no rainbows, men holding hands etc.

The design should be premium, minimalist and not be busy or overwhelming.

I have uploaded a file called "Bottle" to give an idea of the type of container, but please ignore the colours and change as you see fit. This is just for reference for the type of bottle we'll use - all colours are customisable.

I have also uploaded some images for "style" reference, e.g., darvo, quelrin, pia venturek, etc for inspiration.

```html
<!DOCTYPE html>
<html lang="en">
<head>
<meta charset="utf-8">
<title>velnora — label range</title>
<link href="https://fonts.googleapis.com/css2?family=Space+Grotesk:wght@500;600&display=swap" rel="stylesheet">
<style>
  :root {
    --page: #f3f3f3;
    --ink: #2f2f2f;
    --tab: #333333;
    --tab-text: #f2f2f2;
    --gold-a: #b8902a;
    --gold-b: #f3d77a;
    --sage-a: #d3dacf;
    --sage-b: #bcc6b6;
    --mauve-a: #d9d2d1;
    --mauve-b: #bfb3b2;
    --blush-a: #f1e6df;
    --blush-b: #e2cfc3;
  }
  * { box-sizing: border-box; margin: 0; padding: 0; }
  html, body { width: 1200px; height: 658px; overflow: hidden; background: var(--page); }
  .canvas { position: relative; width: 1200px; height: 658px; }

  .label {
    position: absolute; top: 182px; width: 316px; height: 423px;
    color: var(--ink); font-family: "Space Grotesk", sans-serif; font-weight: 500;
  }
  .label::before {
    content: ""; position: absolute; left: 0; right: 0; top: 0; height: 3px;
    background: linear-gradient(90deg, var(--gold-a), var(--gold-b), var(--gold-a));
  }
  .label--sage  { left: 45px;  background: linear-gradient(90deg, var(--sage-a), var(--sage-b)); }
  .label--mauve { left: 445px; background: linear-gradient(90deg, var(--mauve-a), var(--mauve-b)); }
  .label--blush { left: 845px; background: linear-gradient(90deg, var(--blush-a), var(--blush-b)); }

  .wordmark {
    position: absolute; left: 23px; top: 52px;
    font-family: "Space Grotesk", sans-serif; font-weight: 500;
    font-size: 30px; line-height: 34px; letter-spacing: 0.5px;
    color: var(--ink); white-space: nowrap;
  }
  .headline, .tagline {
    position: absolute; left: 23px; font-size: 8.8px; line-height: 12px; white-space: nowrap;
  }
  .headline { top: 100px; }
  .tagline { top: 152px; }
  .claim {
    position: absolute; left: 25px; height: 14px; border: 1.2px solid var(--ink);
    font-size: 6.3px; line-height: 12px; padding-left: 4px; white-space: nowrap;
  }
  .claim--benefits { top: 116px; width: 175px; }
  .claim--audience { top: 134px; width: 127px; }

  .tier {
    position: absolute; left: 288px; top: 147px; width: 28px; height: 81px;
    background: var(--tab); color: var(--tab-text);
    display: flex; align-items: center; justify-content: center;
  }
  .tier span {
    font-size: 10px; font-weight: 600; writing-mode: vertical-rl; transform: rotate(180deg);
  }

  .origin { position: absolute; left: 23px; top: 374px; white-space: nowrap; }
  .origin .made { display: block; font-size: 7.5px; }
  .origin .backed { display: block; font-size: 9.4px; margin-top: 2px; }
</style>
</head>
<body>
<main class="canvas">

  <section class="label label--sage">
    <p class="wordmark">velnora</p>
    <p class="headline">Science + technology for modern gut care</p>
    <p class="claim claim--benefits">Supports digestion, regularity &amp; internal cleansing.</p>
    <p class="claim claim--audience">Daily gut health supplement for men</p>
    <p class="tagline">Where science meets self-care</p>
    <div class="tier"><span>premium</span></div>
    <p class="origin"><span class="made">Made in the UK ·</span><span class="backed">Backed by science</span></p>
  </section>

  <section class="label label--mauve">
    <p class="wordmark">velnora</p>
    <p class="headline">Science + technology for modern gut care</p>
    <p class="claim claim--benefits">Supports digestion, regularity &amp; internal cleansing.</p>
    <p class="claim claim--audience">Daily gut health supplement for men</p>
    <p class="tagline">Where science meets self-care</p>
    <div class="tier"><span>premium</span></div>
    <p class="origin"><span class="made">Made in the UK ·</span><span class="backed">Backed by science</span></p>
  </section>

  <section class="label label--blush">
    <p class="wordmark">velnora</p>
    <p class="headline">Science + technology for modern gut care</p>
    <p class="claim claim--benefits">Supports digestion, regularity &amp; internal cleansing.</p>
    <p class="claim claim--audience">Daily gut health supplement for men</p>
    <p class="tagline">Where science meets self-care</p>
    <div class="tier"><span>premium</span></div>
    <p class="origin"><span class="made">Made in the UK ·</span><span class="backed">Backed by science</span></p>
  </section>

</main>
</body>
</html>
```